Construction company that specializes in roofing and siding

https://havenridgeroofs.example/featured-projects/

https://www.pinecrestrenovationllc.example/#

https://www.ironmeadowhomes.example/residential-siding-services/

Please model a website after these examples
I posted a doc that has some content to get you started. I will upload more content and photos as the site progresses.

Coded - Design and coding required

5+ page

```html
<!DOCTYPE html>
<html lang="en">
<head>
<meta charset="utf-8">
<title>Stonebridge Construction</title>
<link href="https://fonts.googleapis.com/css2?family=Poppins:wght@400;500;600&family=Lato:wght@400;700&display=swap" rel="stylesheet">
<style>
:root{
  --blue:#0a5fad;
  --blue-dark:#084b8a;
  --ink:#1f2a3a;
  --text:#555b66;
  --muted:#8a8f98;
  --light:#f5f6f8;
  --footer:#24252a;
  --white:#ffffff;
}
*{margin:0;padding:0;box-sizing:border-box}
html,body{width:1200px;height:2956px;overflow:hidden}
body{position:relative;background:var(--white);font-family:'Lato',sans-serif;color:var(--text)}
.abs{position:absolute}
.heading{font-family:'Poppins',sans-serif;color:var(--ink);font-weight:500}
.btn{position:absolute;display:flex;align-items:center;justify-content:center;background:var(--blue);color:var(--white);font-family:'Poppins',sans-serif;font-weight:600;font-size:11px;letter-spacing:.5px;text-transform:uppercase}
.eyebrow{font-family:'Poppins',sans-serif;font-weight:600;font-size:11px;letter-spacing:.5px;text-transform:uppercase}

/* header */
.site-header{top:0;left:0;width:1200px;height:70px;background:var(--white)}
.brand{display:flex;align-items:center;gap:10px}
.brand-mark{width:18px;height:18px;background:var(--ink)}
.brand-name{font-family:'Poppins',sans-serif;font-weight:600;font-size:18px;letter-spacing:1px;color:var(--ink)}
.nav{top:27px;left:492px;display:flex;gap:36px;font-family:'Poppins',sans-serif;font-size:10.5px;font-weight:500;color:var(--ink);letter-spacing:.4px}
.quote-btn{left:958px;top:18px;width:130px;height:35px;font-size:12.5px;font-weight:500;text-transform:none;letter-spacing:0}

/* hero */
.hero{top:70px;left:0;width:1200px;height:440px;background:linear-gradient(90deg,#1b222c 0%,#2a3340 45%,#5a4a3c 70%,#30363f 100%)}
.hero-eyebrow{left:112px;top:176px;color:var(--white);font-size:10px}
.hero-title{left:112px;top:198px;color:var(--white);font-size:39px;line-height:44px;font-weight:600}
.hero-text{left:112px;top:297px;width:430px;color:var(--white);font-size:13px;line-height:23px}
.hero-btn{left:112px;top:369px;width:156px;height:39px;font-size:10px}
.hero-arrow{left:0;top:267px;width:33px;height:42px;background:rgba(0,0,0,.35)}
.dots{display:flex;gap:9px}
.dot{width:10px;height:10px;border-radius:50%;background:rgba(255,255,255,.8)}
.dot.on{background:var(--blue)}
.share{left:1158px;top:237px;width:42px}
.share span{display:block;width:42px;height:42px;margin-bottom:1px;background:var(--blue)}
.share span.grey{background:#c8cbd0}

/* highlights */
.highlights{top:510px;left:0;width:1200px;height:167px;background:var(--light)}
.highlight{position:absolute;top:27px;width:300px}
.highlight svg{position:absolute;left:0;top:0}
.highlight h3{position:absolute;left:84px;top:30px;font-size:18px;white-space:nowrap}
.highlight p{position:absolute;left:0;top:66px;width:300px;font-size:12px;line-height:23px}

/* about */
.about-title{left:112px;top:803px;font-size:28px;line-height:37px;width:430px}
.about-btn{left:112px;top:932px;width:145px;height:39px;font-size:10px}
.promise-title{left:614px;top:786px;font-size:25px}
.promise-text{left:614px;top:834px;width:474px;font-size:13px;line-height:23px}
.sign{right:112px;text-align:right;font-size:13px;color:var(--ink)}

/* services */
.services-band{top:1098px;left:0;width:1200px;height:307px;background:var(--blue)}
.services-bg{top:1405px;left:0;width:1200px;height:307px;background:var(--light)}
.services-eyebrow{top:1190px;left:0;width:1200px;text-align:center;color:var(--white)}
.services-title{top:1216px;left:0;width:1200px;text-align:center;color:var(--white);font-size:29px;line-height:38px}
.cards{top:1327px;left:112px;width:976px;height:296px;background:var(--white);box-shadow:0 6px 24px rgba(0,0,0,.08);display:flex}
.card{flex:1;position:relative;text-align:center;border-right:1px solid #eef0f3}
.card:last-child{border-right:none}
.card svg{margin-top:38px}
.card h4{font-family:'Poppins',sans-serif;font-weight:500;font-size:16px;color:var(--ink);margin-top:12px}
.card p{font-size:12.5px;line-height:23px;color:var(--muted);width:190px;margin:14px auto 0}
.card .btn{left:62px;top:223px;width:119px;height:37px;font-size:10px}
.slider-arrow{top:1458px;width:43px;height:42px;background:var(--white);box-shadow:0 2px 8px rgba(0,0,0,.12);display:flex;align-items:center;justify-content:center}

/* banner */
.banner{top:1712px;left:0;width:1200px;height:358px;background:linear-gradient(90deg,#3a4049 0%,#525760 50%,#3e434b 100%)}
.banner-eyebrow{top:1804px;left:0;width:1200px;text-align:center;color:var(--white);font-size:9px}
.banner-title{top:1832px;left:0;width:1200px;text-align:center;color:var(--white);font-size:38px;line-height:42px;font-weight:600}
.banner-btn{left:525px;top:1943px;width:149px;height:39px;font-size:10px}

/* testimonials */
.testimonials{top:2070px;left:0;width:1200px;height:485px;background-color:#fafbfc;background-image:radial-gradient(#e4e7ec 1px,transparent 1px);background-size:9px 9px}
.t-eyebrow{top:2162px;left:0;width:1200px;text-align:center;color:var(--ink)}
.t-title{top:2188px;left:0;width:1200px;text-align:center;font-size:28px}
.t-card{top:2262px;width:484px;height:203px;background:var(--white);border-left:3px solid var(--blue);box-shadow:0 4px 18px rgba(0,0,0,.06)}
.avatar{position:absolute;left:27px;top:58px;width:88px;height:88px;border-radius:50%}
.t-quote{position:absolute;left:133px;top:30px;width:320px;font-size:12.5px;line-height:23px;color:var(--muted)}
.t-name{position:absolute;left:133px;top:133px;font-family:'Poppins',sans-serif;font-weight:500;font-size:14px;color:var(--ink)}
.t-name b{color:var(--blue);letter-spacing:2px;font-size:11px;margin-left:6px}
.t-role{position:absolute;left:133px;top:160px;font-size:9px;color:var(--muted);letter-spacing:.5px}
.t-mark{position:absolute;right:24px;top:140px;font-family:'Poppins',sans-serif;font-size:84px;line-height:84px;color:var(--blue);font-weight:600;height:44px;overflow:hidden}
.t-dots{top:2495px;left:588px;display:flex;gap:4px}
.t-dots span{width:9px;height:8px;background:#3c4656}
.t-dots span.on{background:var(--blue)}

/* footer */
.site-footer{top:2555px;left:0;width:1200px;height:401px;background:var(--footer);color:#b9bcc3}
.footer-brand .brand-name{color:var(--white)}
.footer-brand .brand-mark{background:var(--white)}
.f-text{font-size:12.5px;line-height:23px}
.f-head{font-family:'Poppins',sans-serif;font-weight:500;font-size:14px;color:var(--white)}
.f-links{list-style:none;font-size:12.5px;line-height:27px}
.news-input{left:780px;top:2735px;width:192px;height:43px;background:var(--white);font-size:11px;color:#b0b4bb;padding:15px 10px}
.news-btn{left:972px;top:2735px;width:116px;height:43px;font-size:10px}
.to-top{left:1116px;top:2872px;width:40px;height:40px;border-radius:50%;background:var(--blue)}
.copyright{top:2916px;left:0;width:1200px;text-align:center;font-size:9px;color:#b9bcc3;letter-spacing:.2px}
.copyright a{color:var(--blue);text-decoration:none}
</style>
</head>
<body>

<header class="abs site-header">
  <div class="abs brand" style="left:115px;top:24px">
    <span class="brand-mark"></span><span class="brand-name">STONEBRIDGE</span>
  </div>
  <nav class="abs nav">
    <span>HOME</span><span>ABOUT</span><span>WHAT WE DO</span><span>CLIENTS REVIEWS</span><span>CONTACT</span>
  </nav>
  <div class="btn quote-btn">Request a Quote</div>
</header>

<section class="abs hero" role="img" aria-label="Photo of two builders in orange hard hats reviewing plans on a site"></section>
<div class="abs eyebrow hero-eyebrow">Residencial</div>
<h1 class="abs heading hero-title">We provide outstanding<br>construction services.</h1>
<p class="abs hero-text">We have provided complete remodeling and construction solutions for residential and commercial properties in cities.</p>
<div class="btn hero-btn">View Projects&nbsp;&nbsp;→</div>
<div class="abs hero-arrow"><svg width="33" height="42"><path d="M19 16l-5 5 5 5" stroke="#fff" stroke-width="2" fill="none"/></svg></div>
<div class="abs dots" style="left:572px;top:475px"><span class="dot on"></span><span class="dot"></span><span class="dot"></span></div>
<div class="abs share">
  <span></span><span></span><span></span>
  <span class="grey"><svg width="42" height="42"><rect x="10" y="13" width="22" height="16" fill="none" stroke="#fff" stroke-width="2"/><path d="M10 13l11 9 11-9" stroke="#fff" stroke-width="2" fill="none"/></svg></span>
</div>

<section class="abs highlights">
  <div class="highlight" style="left:112px">
    <svg width="48" height="44" viewBox="0 0 48 44" fill="none" stroke="#2a3340" stroke-width="1.6"><path d="M3 42V4h6v38M9 42V20l10 6v-6l10 6v-6l10 6v16M1 42h46"/><rect x="14" y="32" width="5" height="5"/><rect x="24" y="32" width="5" height="5"/><rect x="34" y="32" width="5" height="5"/></svg>
    <h3 class="heading">Professional Liability</h3>
    <p>We are committed to building a sustainable future by fostering a collaborative spirit.</p>
  </div>
  <div class="highlight" style="left:446px">
    <svg width="48" height="44" viewBox="0 0 48 44" fill="none" stroke="#2a3340" stroke-width="1.6"><path d="M10 18a14 14 0 0128 0M6 18h36M20 6h8v8h-8zM10 42c0-8 6-14 14-14s14 6 14 14"/></svg>
    <h3 class="heading">Dedicated To Our Clients</h3>
    <p>We are committed to building a sustainable future by fostering a collaborative spirit.</p>
  </div>
  <div class="highlight" style="left:780px">
    <svg width="48" height="44" viewBox="0 0 48 44" fill="none" stroke="#2a3340" stroke-width="1.6"><circle cx="22" cy="22" r="8"/><circle cx="22" cy="22" r="4"/><circle cx="22" cy="22" r="15" stroke-dasharray="5 3"/><circle cx="22" cy="22" r="19"/></svg>
    <h3 class="heading">Outstanding Services</h3>
    <p>We are committed to building a sustainable future by fostering a collaborative spirit.</p>
  </div>
</section>

<h2 class="abs heading about-title">Stonebridge Construction is your source for roofing and siding in Minnesota.</h2>
<div class="btn about-btn">More About Us</div>
<h2 class="abs heading promise-title">The Stonebridge Promise</h2>
<p class="abs promise-text">You deserve timely service, high quality materials, expert installation, and a stonebridge warranty. That is what we promise to deliver. I invite you to put us to the test today.</p>
<p class="abs sign" style="top:917px">Sincerely,</p>
<p class="abs sign" style="top:953px;font-weight:700">Dale Harmon, Owner</p>
<p class="abs sign" style="top:976px;font-weight:700">Stonebridge Construction</p>

<section class="abs services-band" role="img" aria-label="Faint world map texture on blue"></section>
<div class="abs services-bg"></div>
<div class="abs eyebrow services-eyebrow">What We Do</div>
<h2 class="abs heading services-title">Take the world’s best<br>services for you</h2>
<div class="abs slider-arrow" style="left:52px"><svg width="8" height="10"><path d="M6 1L2 5l4 4z" fill="#1f2a3a"/></svg></div>
<div class="abs slider-arrow" style="left:1105px"><svg width="8" height="10"><path d="M2 1l4 4-4 4z" fill="#1f2a3a"/></svg></div>
<div class="abs cards">
  <div class="card">
    <svg width="44" height="52" viewBox="0 0 44 52" fill="none" stroke="#0a5fad" stroke-width="2.5"><path d="M4 50V18L22 4l18 14v32zM4 18l32 32M14 50V32"/></svg>
    <h4>Roofing</h4><p>We are committed to a sustainable future fostering a collaborative spirit.</p>
    <div class="btn">Read More</div>
  </div>
  <div class="card">
    <svg width="44" height="52" viewBox="0 0 44 52" fill="none" stroke="#0a5fad" stroke-width="2.5"><path d="M4 4h36v10H4zM4 14h36v10H4zM4 24h36v10H4zM4 34h36v10H4zM4 44h36v6H4z"/></svg>
    <h4>Siding</h4><p>We are committed to a sustainable future fostering a collaborative spirit.</p>
    <div class="btn">Read More</div>
  </div>
  <div class="card">
    <svg width="44" height="52" viewBox="0 0 44 52" fill="none" stroke="#0a5fad" stroke-width="2.5"><path d="M2 6h40v8H2zM30 14v10l-8 8v18h-8V30l8-8v-8"/></svg>
    <h4>Gutters</h4><p>We are committed to a sustainable future fostering a collaborative spirit.</p>
    <div class="btn">Read More</div>
  </div>
  <div class="card">
    <svg width="44" height="52" viewBox="0 0 44 52" fill="none" stroke="#0a5fad" stroke-width="2.5"><path d="M4 4h36v44H4zM8 8h28v36H8zM22 8v36M8 8c4 10 8 20 10 36M36 8c-4 10-8 20-10 36"/></svg>
    <h4>Windows</h4><p>We are committed to a sustainable future fostering a collaborative spirit.</p>
    <div class="btn">Read More</div>
  </div>
</div>

<section class="abs banner" role="img" aria-label="Dimmed photo of a bright modern living room with a sofa and window"></section>
<div class="abs eyebrow banner-eyebrow">Explore The Features</div>
<h2 class="abs heading banner-title">The best constructions<br>company since 2016</h2>
<div class="btn banner-btn">Get Free Quote</div>

<section class="abs testimonials"></section>
<div class="abs eyebrow t-eyebrow">Testimonial</div>
<h2 class="abs heading t-title">What people says</h2>
<article class="abs t-card" style="left:112px">
  <div class="avatar" role="img" aria-label="Portrait photo of Marta Lindqvist" style="background:linear-gradient(135deg,#d9c2a4,#8a6d52)"></div>
  <p class="t-quote">"Thank you for guiding us through the construction process, understanding, and always ready to accommodate our needs. We love our new space and know that it was built by the very best!"</p>
  <div class="t-name">Marta Lindqvist<b>★★★★★</b></div>
  <div class="t-role">DIRECTOR</div>
  <div class="t-mark">”</div>
</article>
<article class="abs t-card" style="left:604px">
  <div class="avatar" role="img" aria-label="Portrait photo of Owen Brightwell" style="background:linear-gradient(135deg,#4a6f9a,#1e2b3d)"></div>
  <p class="t-quote">"Thank you for guiding us through the construction process, understanding, and always ready to accommodate our needs. We love our new space and know that it was built by the very best!"</p>
  <div class="t-name">Owen Brightwell<b>★★★★★</b></div>
  <div class="t-role">DIRECTOR</div>
  <div class="t-mark">”</div>
</article>
<div class="abs t-dots"><span></span><span class="on"></span></div>

<footer class="abs site-footer"></footer>
<div class="abs brand footer-brand" style="left:112px;top:2658px">
  <span class="brand-mark"></span><span class="brand-name">STONEBRIDGE</span>
</div>
<p class="abs f-text" style="left:112px;top:2703px;width:240px;color:#b9bcc3">Stonebridge Construction is your source for roofing and siding in Minnesota.</p>
<div class="btn" style="left:112px;top:2762px;width:120px;height:38px;font-size:10px">Read More</div>

<h5 class="abs f-head" style="left:363px;top:2644px">Company</h5>
<ul class="abs f-links" style="left:363px;top:2675px;color:#b9bcc3">
  <li>About Us</li><li>What We Do</li><li>Clients Reviews</li><li>Contact Us</li>
</ul>

<h5 class="abs f-head" style="left:530px;top:2644px">Headquaters</h5>
<p class="abs f-text" style="left:530px;top:2676px;width:230px;color:#b9bcc3">48 Cedar Lane, 2nd Floor, Northfield, 55057</p>
<p class="abs f-text" style="left:530px;top:2734px;color:var(--blue)">info@stonebridge.example</p>
<p class="abs f-text" style="left:530px;top:2757px;color:#b9bcc3">(+1) 555 014 2290</p>

<h5 class="abs f-head" style="left:780px;top:2644px">Newslatter Subscription</h5>
<p class="abs f-text" style="left:780px;top:2676px;width:240px;color:#b9bcc3">Subscribe and get 10% off from our construction company.</p>
<div class="abs news-input">Enter Your Email Address...</div>
<div class="btn news-btn">Subscribe</div>

<div class="abs to-top"><svg width="40" height="40"><path d="M16 22l4-4 4 4" stroke="#fff" stroke-width="2" fill="none"/></svg></div>
<p class="abs copyright">COPYRIGHT © <a>STONEBRIDGE CONSTRUCTION</a>. ALL RIGHTS RESERVED.</p>

</body>
</html>
```